Elder Care Rate and Services flyer

We are looking for a flyer to print and mail out, I have attached the long version that we are trying to shorten to give the information that the person needs with rates and services in color, this should look similar to our Golden Years Leaflet you created for us. We want it to be printable and able to email it as well. With this form we do not need as many images. 2 sided flyer
-Logo on both sides
-QR codes to lead to the www.BrightlaneCare.com on both sides
-Contact information: Call: (808) 555-0173 Email: Info@BrightlaneCare.com Website: www.BrightlaneCare.com
Front Page should be about our company and what services we provide:
Founded in 1996, Brightlane Homecare is one of Hawaii’s largest state-licensed home health care agencies. We provide personal care and assistance with the activities of daily living in homes and facilities all across Oahu, ranging from personal care to skilled nursing.
Our mission is to provide our clients with dependable, compassionate, and professional care in the comfort of your home. We strive to meet the individual needs of our clients, encouraging independence, preserving dignity, and nurturing the spirit of our island community.
Brightlane Homecare Skilled Nurses and Caregivers are bonded, insured, certified in CPR and First Aid. TB-screened, pass criminal and abuse background checks, and most importantly, are caring and compassionate.
-Skilled Nursing & Medication Services
-Turning, Repositioning, & Transfers
-Bathing/Showering, Dressing & Grooming
-Simple Meal Preparation & Feeding
-Light Housekeeping & Laundry
-Personal Care Services Available 24/7
-Driving to Appointments, Errands, Outings
Side 2: Rates of services
Please see attached sample for back side, No need for so many images and the logo needs to be bigger.

Target Market(s)

Ages 35-105 Male and Female

Industry/Entity Type

Senior In-Home Care

Font styles to use
Sans Serif

Colors
00AB8E
00BBA5
67D7C9
C6EFE9
E9F9F6

Requirements
Must have
• Our logo and contact information
Nice to have
• Located in Hawaii, nice for images to have a local feel
Should not have
• no images of sick people

```html
<!DOCTYPE html>
<html lang="en">
<head>
<meta charset="utf-8">
<title>Brightlane Homecare – Services and Rates Flyer</title>
<link href="https://fonts.googleapis.com/css2?family=Roboto:ital,wght@0,300;0,400;0,500;0,700;1,400&display=swap" rel="stylesheet">
<style>
:root{
  --teal-dark:#0f5f5a;
  --teal:#1f8a84;
  --salmon:#f59c99;
  --salmon-deep:#e9686b;
  --salmon-soft:#f7c9c6;
  --mint:#a9ddd9;
  --sand:#f3ead6;
  --ink:#1d1d1d;
  --paper:#ffffff;
  --backdrop:#f1f1f1;
}
*{box-sizing:border-box;margin:0;padding:0}
html,body{width:1200px;height:3000px;overflow:hidden}
body{background:var(--backdrop);font-family:"Roboto",sans-serif;color:var(--ink);position:relative}
.page{position:absolute;left:100px;width:1000px;height:1300px;background:var(--paper);overflow:hidden;box-shadow:0 6px 18px rgba(0,0,0,.25)}
.page--front{top:150px}
.page--back{top:1550px}
.abs{position:absolute}
.photo{position:absolute}
svg.shape{position:absolute;left:0;top:0}

/* brand block */
.brand{position:absolute;text-align:center}
.brand__row{display:flex;align-items:center;justify-content:center;gap:14px}
.brand__mark{width:30px;height:30px;background:var(--salmon)}
.brand__name{font-weight:700;color:var(--teal-dark);line-height:1}
.brand__tagline{font-style:italic;color:var(--teal-dark);line-height:1.3;margin-top:14px}

/* front: headings */
.h-light{font-weight:300;font-size:32px;color:var(--ink);letter-spacing:.5px}
.h-bold{font-weight:700;font-size:34px;color:var(--teal-dark);letter-spacing:.5px}
.body-copy{font-size:14.5px;line-height:1.2;color:var(--ink)}

.services-title{font-size:36px;color:var(--teal-dark);font-weight:400}
.services-title b{font-weight:500}
.service{position:absolute;display:flex;align-items:center;gap:18px;font-size:14.5px;color:var(--ink);line-height:1.15}
.service__icon{width:30px;height:30px;border-radius:50%;background:var(--paper);opacity:.85;flex:none}
.service-rule{position:absolute;height:0;border-top:2px dotted rgba(255,255,255,.8)}

.skilled{position:absolute;left:0;top:913px;width:501px;height:244px;background:var(--teal-dark);color:var(--paper)}
.skilled__title{position:absolute;left:20px;top:22px;font-size:34px;font-weight:300}
.skilled__title b{font-weight:500}
.skilled__sub{position:absolute;left:20px;top:66px;font-size:21px;font-weight:500}
.skilled__sub::after{content:"";display:inline-block;width:65px;border-top:2px dotted var(--paper);margin-left:16px;vertical-align:middle}
.trait{position:absolute;display:flex;align-items:center;gap:18px;font-size:16px}
.trait__icon{width:52px;height:52px;border-radius:50%;border:2px dotted var(--paper);display:flex;align-items:center;justify-content:center}
.trait__icon::after{content:"";width:24px;height:24px;border-radius:50%;background:var(--salmon-deep)}

/* footer */
.footer{position:absolute;left:0;bottom:0;width:1000px;height:76px;background:var(--teal-dark);color:var(--paper);display:flex;align-items:center}
.footer__phone{position:absolute;left:10px;top:10px;width:320px;height:54px;background:var(--paper);border-radius:27px;display:flex;align-items:center;gap:24px;padding-left:26px;font-size:27px;color:var(--teal-dark)}
.footer__item{position:absolute;display:flex;align-items:center;gap:12px;font-size:14px}
.footer__web{letter-spacing:2px}
.social{position:absolute;width:28px;height:28px;border-radius:50%;background:var(--salmon-deep)}

/* back */
.rates-title{position:absolute;left:30px;top:448px;font-size:34px;font-weight:300;color:var(--ink)}
.rates-title b{font-weight:700;color:var(--teal-dark)}
table.rates{position:absolute;left:28px;top:507px;width:941px;border-collapse:collapse;font-size:15px}
table.rates th{height:32px;font-weight:400;font-size:16px;text-align:center}
table.rates th.col-level{background:var(--salmon-deep);text-align:left;padding-left:4px}
table.rates th.col-shift{background:var(--mint)}
table.rates th.col-ind{background:var(--sand)}
table.rates th.col-cpl{background:var(--salmon-soft)}
table.rates td{height:35px;text-align:center;border-bottom:2px dotted #9a9a9a;border-right:2px dotted #9a9a9a}
table.rates td:first-child{text-align:left;padding-left:4px;background:#f4f4f4;border-right:none}
table.rates td:last-child{border-right:none}
.note{position:absolute;left:35px;width:930px;font-size:12.5px;line-height:1.3}
.med-title{position:absolute;left:28px;top:958px;font-size:34px;font-weight:300;line-height:1.1}
.med-title b{font-weight:700;color:var(--teal-dark)}
.med-title span{font-weight:500;color:var(--ink);font-size:30px;margin-left:12px}
.med-copy{position:absolute;left:25px;top:1072px;width:375px;font-size:13.5px;line-height:1.25}
.add-title{position:absolute;left:535px;top:970px;font-size:33px;font-weight:300}
.add-title b{font-weight:700;color:var(--teal-dark)}
.add-table{position:absolute;left:412px;top:1012px;width:556px;height:128px;border:2px dotted #9a9a9a;display:grid;grid-template-columns:1fr 1fr;grid-template-rows:30px 1fr}
.add-table__head{color:var(--paper);font-weight:500;font-size:18px;display:flex;align-items:center;justify-content:center}
.add-table__head--ind{background:var(--salmon-deep)}
.add-table__head--cpl{background:var(--teal)}
.add-table__cell{padding:6px 0 0 22px;font-size:15px;line-height:1.55}
.add-table__cell + .add-table__cell{border-left:2px dotted #9a9a9a}
</style>
</head>
<body>

<!-- FRONT SIDE -->
<section class="page page--front">
  <svg class="shape" width="1000" height="1300" viewBox="0 0 1000 1300" aria-hidden="true">
    <path d="M0 0 H535 C575 180 560 400 470 470 C360 540 120 510 0 460 Z" fill="#d77a7a"/>
    <path d="M0 0 H520 C560 180 545 390 460 458 C355 525 120 500 0 448 Z" fill="#8aa6b6"/>
    <path d="M0 448 C120 500 355 525 460 458 L470 470 C360 545 120 520 0 470 Z" fill="var(--teal-dark)"/>
    <path d="M501 410 C600 320 760 270 880 300 C940 315 980 345 1000 370 V1228 H501 Z" fill="var(--salmon)"/>
    <path d="M540 360 C650 280 800 250 900 285 C960 305 990 335 1000 355 V400 C980 360 940 330 880 318 C760 290 620 330 540 360 Z" fill="var(--teal-dark)"/>
  </svg>
  <div class="photo" role="img" aria-label="Caregiver in a mask reviewing a tablet with an older man at home" style="left:0;top:0;width:1px;height:1px"></div>
  <svg class="shape" width="1000" height="1300" aria-hidden="true">
    <circle cx="469" cy="414" r="134" fill="var(--teal)"/>
    <circle cx="469" cy="414" r="126" fill="#c9b48e"/>
  </svg>
  <div class="photo" role="img" aria-label="Residents and a caregiver relaxing together in a bright living room" style="left:343px;top:288px;width:252px;height:252px;border-radius:50%"></div>

  <div class="brand" style="left:560px;top:20px;width:420px">
    <div class="brand__row"><span class="brand__mark"></span><span class="brand__name" style="font-size:50px">Brightlane Homecare</span></div>
    <div class="brand__tagline" style="font-size:19px">Someone you can depend on...<br>Without question</div>
  </div>

  <div class="abs h-light" style="left:22px;top:535px">ABOUT</div>
  <div class="abs h-bold" style="left:22px;top:573px">BRIGHTLANE CARE GROUP</div>
  <p class="abs body-copy" style="left:22px;top:643px;width:455px">Founded in 1996, Brightlane Homecare is one of Hawaii's largest state-licensed home health care agencies. We provide personal care and assistance with the activities of daily living in homes and facilities all across Oahu, ranging from personal care to skilled nursing.</p>
  <div class="abs h-light" style="left:22px;top:730px">OUR</div>
  <div class="abs h-bold" style="left:22px;top:768px">MISSION</div>
  <p class="abs body-copy" style="left:20px;top:828px;width:470px">Our mission is to provide our clients with dependable, compassionate, and professional care in the comfort of your home. We strive to meet the individual needs of our clients, encouraging independence, preserving dignity, and nurturing the spirit of our island community.</p>

  <div class="skilled">
    <div class="skilled__title">OUR <b>SKILLED</b></div>
    <div class="skilled__sub">Nurses and Caregivers are</div>
    <div class="trait" style="left:20px;top:106px"><span class="trait__icon"></span>Insured</div>
    <div class="trait" style="left:270px;top:106px"><span class="trait__icon"></span>First Aid</div>
    <div class="trait" style="left:20px;top:172px"><span class="trait__icon"></span>Bonded</div>
    <div class="trait" style="left:270px;top:172px"><span class="trait__icon"></span>Certified in CPR</div>
  </div>
  <p class="abs" style="left:24px;top:1172px;width:470px;font-size:17px;line-height:1.25">TB-screened, pass criminal and abuse backgroundchecks, and most importantly, are caring and compassionate.</p>

  <div class="abs services-title" style="left:653px;top:444px">Our <b>services</b></div>
  <div class="service" style="left:540px;top:542px"><span class="service__icon"></span>Light Housekeeping</div>
  <div class="service" style="left:762px;top:532px"><span class="service__icon"></span>Bathing/Showering,<br>Grooming</div>
  <div class="service-rule" style="left:560px;top:592px;width:410px"></div>
  <div class="service" style="left:540px;top:613px"><span class="service__icon"></span>Skilled Nursing</div>
  <div class="service" style="left:762px;top:613px"><span class="service__icon"></span>Outings</div>
  <div class="service-rule" style="left:560px;top:660px;width:410px"></div>
  <div class="service" style="left:540px;top:690px"><span class="service__icon"></span>Medication Services</div>
  <div class="service" style="left:762px;top:680px"><span class="service__icon"></span>Turning, Repositioning,<br>&amp; Transfers</div>
  <div class="service-rule" style="left:560px;top:738px;width:410px"></div>
  <div class="service" style="left:540px;top:760px"><span class="service__icon"></span>Laundry</div>
  <div class="service" style="left:762px;top:744px"><span class="service__icon"></span>Simple Meal<br>Preparation<br>&amp; Feeding</div>
  <div class="service-rule" style="left:560px;top:808px;width:410px"></div>
  <div class="service" style="left:540px;top:830px"><span class="service__icon"></span>Driving to<br>Appointments,<br>Errands, Outings</div>
  <div class="service" style="left:762px;top:840px"><span class="service__icon"></span>Personal Care<br>Services Available 24/7</div>
  <div class="service-rule" style="left:560px;top:896px;width:410px"></div>

  <div class="photo" role="img" aria-label="Smiling nurse with her hand on the shoulder of a happy older woman" style="left:585px;top:900px;width:400px;height:328px;background:linear-gradient(160deg,#f7b3ae 0%,#e9d9cf 45%,#6fb3d2 100%);border-radius:180px 180px 0 0"></div>

  <footer class="footer">
    <div class="footer__phone"><svg width="28" height="28" viewBox="0 0 24 24" aria-hidden="true"><path d="M6.6 10.8a15 15 0 006.6 6.6l2.2-2.2a1 1 0 011-.25 11.4 11.4 0 003.6.57 1 1 0 011 1V20a1 1 0 01-1 1A17 17 0 013 4a1 1 0 011-1h3.5a1 1 0 011 1c0 1.25.2 2.45.57 3.6a1 1 0 01-.25 1z" fill="var(--salmon-deep)"/></svg>(808) 555-0173</div>
    <div class="footer__item" style="left:362px;top:28px"><svg width="26" height="18" viewBox="0 0 26 18" aria-hidden="true"><rect x="1" y="1" width="24" height="16" fill="none" stroke="var(--salmon-deep)" stroke-width="2"/><path d="M1 1l12 9 12-9" fill="none" stroke="var(--salmon-deep)" stroke-width="2"/></svg>Info@BrightlaneCare.com</div>
    <div class="footer__item footer__web" style="left:575px;top:27px"><svg width="24" height="24" viewBox="0 0 24 24" aria-hidden="true"><circle cx="12" cy="12" r="10" fill="none" stroke="var(--salmon-deep)" stroke-width="2"/><path d="M2 12h20M12 2c4 4 4 16 0 20M12 2c-4 4-4 16 0 20" fill="none" stroke="var(--salmon-deep)" stroke-width="2"/></svg>www.BrightlaneCare.com</div>
    <span class="social" style="left:853px;top:24px"></span>
    <span class="social" style="left:888px;top:24px"></span>
  </footer>
</section>

<!-- BACK SIDE -->
<section class="page page--back">
  <div class="photo" role="img" aria-label="Close view of a caring hand resting on an older woman's shoulder" style="left:440px;top:0;width:560px;height:320px;background:linear-gradient(120deg,#e4e6ea 0%,#c9b3a6 55%,#7d6f88 100%)"></div>
  <svg class="shape" width="1000" height="1300" viewBox="0 0 1000 1300" aria-hidden="true">
    <path d="M0 0 H470 C455 120 470 260 480 330 C360 360 150 380 0 400 Z" fill="var(--paper)"/>
    <path d="M0 400 C150 380 360 345 470 330 C600 300 800 240 1000 300 V330 C820 270 620 320 470 350 C360 372 150 400 0 420 Z" fill="var(--teal-dark)"/>
    <circle cx="572" cy="328" r="126" fill="var(--salmon-deep)"/>
    <circle cx="572" cy="328" r="119" fill="#c7a07e"/>
    <circle cx="800" cy="373" r="114" fill="var(--salmon-deep)"/>
    <circle cx="800" cy="373" r="107" fill="#9fc4d6"/>
  </svg>
  <div class="photo" role="img" aria-label="Caregiver serving a meal to seniors at a dining table" style="left:453px;top:209px;width:238px;height:238px;border-radius:50%"></div>
  <div class="photo" role="img" aria-label="Silhouette of a person in a wheelchair by the seaside" style="left:693px;top:266px;width:214px;height:214px;border-radius:50%"></div>

  <div class="brand" style="left:20px;top:70px;width:420px">
    <div class="brand__row"><span class="brand__mark" style="width:40px;height:40px"></span><span class="brand__name" style="font-size:56px">Brightlane</span></div>
    <div class="brand__name" style="font-size:44px;margin-top:8px">Homecare</div>
    <div class="brand__tagline" style="font-size:24px">Someone you can depend on...<br>Without question</div>
  </div>

  <div class="rates-title">SERVICE <b>RATES</b></div>
  <table class="rates">
    <thead>
      <tr><th class="col-level" style="width:252px">Level of Care</th><th class="col-shift" style="width:232px">Shift Length</th><th class="col-ind" style="width:228px">Individual Care</th><th class="col-cpl">Couples Care</th></tr>
    </thead>
    <tbody>
      <tr><td>Nurse Aide — Bath Service</td><td>2 Hours</td><td>$79.00 / flat rate</td><td>n/a</td></tr>
      <tr><td>Nurse Aide — Be Well</td><td>3 Hours (Minimum)</td><td>$41.00 / hour</td><td>n/a</td></tr>
      <tr><td>Nurse Aide</td><td>3 Hours (Minimum)</td><td>$31.00 / hour</td><td>$41.00 / hour</td></tr>
      <tr><td>Nurse Aide</td><td>4—11 Hours</td><td>$30.00 / hour</td><td>$40.00 / hour</td></tr>
      <tr><td>Nurse Aide</td><td>12—24 Hours</td><td>$29.00 / hour</td><td>$39.00 / hour</td></tr>
      <tr><td>Licensed Practical Nurse (LPN)</td><td>2 Hours (Minimum</td><td>$49.00 / hour</td><td>$69.00 / hour</td></tr>
      <tr><td>Registered Nurse (RN)</td><td>2 Hours (Minimum)</td><td>$62.00 / hour</td><td>$82.00 / hour</td></tr>
    </tbody>
  </table>
  <p class="note" style="top:825px">*Early release of the Care Professional from a shift is subject to the minimum shiftlength charge. Unscheduled shift extensions must be approved by the client and shall be billed in 15-minute increments.</p>
  <p class="note" style="top:878px">The above rates do not include General Excise Tax of 4.188% and County Surcharge Taxof .524%. These taxes shall be applied to the invoice. Rates are subject to change withadvance written notice.</p>

  <div class="med-title">Medication<br><b>Services –</b><span>28-Day Cycle</span></div>
  <p class="med-copy">Brightlane Homecare clients may choose to utilize the services of our licensed nurse to pre-pour medications. Medications shall be pre-poured into weekly pill dispensers for a 28-day period. A list of medications, including over-the-counter medications/supplements will be provided to the client's physician for written authorization.</p>

  <div class="add-title">Additional <b>Services</b></div>
  <div class="add-table">
    <div class="add-table__head add-table__head--ind">Individual Rate</div>
    <div class="add-table__head add-table__head--cpl">Couples Rate</div>
    <div class="add-table__cell">Initial Set-up Fee $85.00<br>$85.00/monthly visit<br>$65.00/visit<br>(medication changes/revisions)</div>
    <div class="add-table__cell" style="padding-left:8px">Initial Set-up Fee $135.00<br>$135.00/monthly visit<br>$85.00/visit (changes/revisions)</div>
  </div>

  <footer class="footer" style="height:100px">
    <div class="footer__phone" style="top:18px;height:60px;width:320px">
      <svg width="30" height="30" viewBox="0 0 24 24" aria-hidden="true"><path d="M6.6 10.8a15 15 0 006.6 6.6l2.2-2.2a1 1 0 011-.25 11.4 11.4 0 003.6.57 1 1 0 011 1V20a1 1 0 01-1 1A17 17 0 013 4a1 1 0 011-1h3.5a1 1 0 011 1c0 1.25.2 2.45.57 3.6a1 1 0 01-.25 1z" fill="var(--salmon-deep)"/></svg>(808) 555-0173</div>
    <div class="footer__item" style="left:362px;top:38px"><svg width="26" height="18" viewBox="0 0 26 18" aria-hidden="true"><rect x="1" y="1" width="24" height="16" fill="none" stroke="var(--salmon-deep)" stroke-width="2"/><path d="M1 1l12 9 12-9" fill="none" stroke="var(--salmon-deep)" stroke-width="2"/></svg>Info@BrightlaneCare.com</div>
    <div class="footer__item footer__web" style="left:630px;top:37px"><svg width="24" height="24" viewBox="0 0 24 24" aria-hidden="true"><circle cx="12" cy="12" r="10" fill="none" stroke="var(--salmon-deep)" stroke-width="2"/><path d="M2 12h20M12 2c4 4 4 16 0 20M12 2c-4 4-4 16 0 20" fill="none" stroke="var(--salmon-deep)" stroke-width="2"/></svg>www.BrightlaneCare.com</div>
    <span class="social" style="left:880px;top:36px"></span>
    <span class="social" style="left:924px;top:36px"></span>
  </footer>
</section>

</body>
</html>
```